Brimvane.com fiber optic internet website redesign

We need a new website design for our fiber optic internet company that provides internet, phone, and tv services. It should use the text "Marrowfen fiber optics", and "I beamed up with Marrowfen". The design should use the color blue and the attached logo.
We are a 30 year old internet company who started as a dial up internet provider in our basement. Today we design, build, and maintain our own fiber optic internet network to provide service to residential, business, educational, healthcare, and governmental customers

```html
<!DOCTYPE html>
<html lang="en">
<head>
<meta charset="UTF-8">
<title>Marrowfen Fiber Optics</title>
<link rel="stylesheet" href="https://fonts.googleapis.com/css2?family=Raleway:wght@600;700;800&family=Inter:wght@400;500;600&display=swap">
<style>
:root{
  --navy:#030a1f;
  --navy-2:#06122e;
  --blue:#0a4fb0;
  --blue-deep:#0842a0;
  --blue-bright:#0d63c4;
  --sky:#7cc4ff;
  --ink:#0b0b14;
  --text:#3b3f4a;
  --pale:#eef5fd;
  --white:#ffffff;
}
*{box-sizing:border-box;margin:0;padding:0}
html,body{width:1200px;height:3305px;overflow:hidden}
body{font-family:"Inter",sans-serif;color:var(--ink);background:var(--white);position:relative}
.heading{font-family:"Raleway",sans-serif;font-weight:800;letter-spacing:-0.5px}
.accent{color:var(--blue-bright)}
.abs{position:absolute}

/* nav */
.site-nav{position:absolute;left:0;top:0;width:1200px;height:80px;background:var(--navy-2);z-index:2}
.site-nav a{position:absolute;top:33px;font-size:11px;color:#c9d3e6;text-decoration:none}
.site-nav a.active{color:#fff;font-weight:600;text-decoration:underline}
.brand{position:absolute;left:540px;top:22px;display:flex;align-items:center;gap:8px;font-family:"Inter",sans-serif;font-weight:600;font-size:16px;color:#fff}
.brand-dot{width:26px;height:26px;border-radius:50%;border:2px solid var(--blue-bright)}
.support-btn{position:absolute;left:1016px;top:26px;width:84px;height:28px;border-radius:14px;background:#fff;color:var(--ink);font-size:11px;font-weight:600;display:flex;align-items:center;justify-content:center}

/* hero */
.hero{position:absolute;left:0;top:80px;width:1200px;height:551px;
  background:radial-gradient(ellipse at 80% 70%,rgba(30,120,120,.55),transparent 45%),
             radial-gradient(ellipse at 30% 95%,rgba(80,80,70,.6),transparent 40%),
             linear-gradient(160deg,#01040e 0%,#020a22 45%,#0a2a6a 80%,#0b3d7a 100%)}
.hero-title{position:absolute;left:103px;top:128px;font-size:58px;line-height:70px;color:#fff}
.hero-title .accent{color:#1c5fd0}
.hero-sub{position:absolute;left:103px;top:285px;width:450px;font-size:14px;line-height:17px;color:#dfe6f3}
.pill{position:absolute;display:flex;align-items:center;justify-content:space-between;border-radius:30px;font-weight:600}
.hero-btn{left:103px;top:354px;width:224px;height:57px;background:var(--blue);color:#fff;font-size:14px;padding:0 6px 0 33px}
.pill-icon{width:44px;height:44px;border-radius:50%;display:flex;align-items:center;justify-content:center}

/* about */
.about{position:absolute;left:0;top:631px;width:1200px;height:475px;background:#fff}
.about h2{position:absolute;left:103px;top:110px;font-size:44px}
.about .lead{position:absolute;left:103px;top:184px;width:490px;font-size:14px;line-height:17px;color:var(--text)}
.fact{position:absolute;top:276px;width:250px}
.fact h3{font-size:18px;font-weight:600;margin-bottom:8px}
.fact p{font-size:14px;line-height:17px;color:var(--text)}
.about-photo{position:absolute;left:699px;top:139px;width:379px;height:216px;border-radius:60px;
  background:radial-gradient(ellipse at 40% 40%,#e36ad6,transparent 50%),linear-gradient(120deg,#3a1a80,#a02fb8 40%,#2a5fd0 70%,#101a60)}
.years{position:absolute;left:681px;top:118px;width:90px;height:90px;border-radius:50%;background:var(--blue);color:#fff;font-family:"Raleway",sans-serif;font-weight:800;font-size:26px;display:flex;align-items:center;justify-content:center}

/* services */
.services{position:absolute;left:0;top:1106px;width:1200px;height:701px;
  background:radial-gradient(ellipse at 20% 60%,rgba(90,140,255,.35),transparent 50%),linear-gradient(180deg,#0a4fb0,#0846a8 60%,#0a4fb5)}
.services h2{position:absolute;left:0;width:1200px;text-align:center;top:98px;font-size:44px;color:#fff}
.services h2 .accent{color:var(--sky)}
.card{position:absolute;width:289px;height:325px;border-radius:18px;padding:0 42px}
.card-ghost{border:1.5px solid rgba(255,255,255,.55);background:rgba(255,255,255,.06);color:#fff}
.card-solid{background:#fff;color:var(--ink)}
.card h3{position:absolute;left:42px;font-family:"Raleway",sans-serif;font-weight:700;font-size:25px}
.card p{position:absolute;left:42px;width:205px;font-size:13px;line-height:17px;font-weight:600}
.card .pill{left:42px;width:205px;height:57px;font-size:13px;padding:0 6px 0 25px}
.btn-white{background:#fff;color:var(--ink)}
.btn-blue{background:var(--blue);color:#fff}
.card-icon{position:absolute;left:50%;transform:translateX(-50%)}

/* customers */
.customers{position:absolute;left:0;top:1807px;width:1200px;height:1151px;background:var(--pale)}
.customers h2{position:absolute;left:0;width:1200px;text-align:center;top:92px;font-size:44px}
.review{position:absolute;top:368px;width:289px;height:331px;border-radius:22px;text-align:center}
.review-light{background:#fff;color:var(--ink)}
.review-dark{background:var(--blue);color:#fff}
.avatar-ring{position:absolute;left:54px;top:-105px;width:180px;height:180px;border-radius:50%;border:1.5px solid #c7d2e2;background:var(--pale);display:flex;align-items:center;justify-content:center}
.avatar{width:152px;height:152px;border-radius:50%}
.stars{position:absolute;top:112px;left:0;width:100%;display:flex;justify-content:center}
.review h4{position:absolute;top:147px;width:100%;font-size:25px;font-weight:500;letter-spacing:-0.4px}
.role{position:absolute;top:186px;width:100%;font-size:17px}
.quote{position:absolute;font-family:"Raleway",sans-serif;font-weight:800;font-size:70px;line-height:1;color:var(--blue)}
.review p{position:absolute;left:28px;width:233px;font-size:13.5px;line-height:17px}
.review-light p{color:var(--text)}
.cta{position:absolute;left:100px;top:781px;width:1000px;height:301px;border-radius:90px;
  background:linear-gradient(110deg,#0b3f9a,#0a4fb0 40%,#0a4ab0 70%,#0b3d98)}
.cta h2{position:absolute;left:0;width:1000px;text-align:center;top:38px;font-size:46px;color:#fff}
.cta p{position:absolute;left:220px;width:560px;top:117px;text-align:center;font-size:13px;line-height:17px;font-weight:600;color:#fff}
.cta .pill{left:387px;top:203px;width:238px;height:57px;background:#fff;color:var(--blue);font-size:13px;padding:0 6px 0 33px}

/* footer */
.site-footer{position:absolute;left:0;top:2958px;width:1200px;height:347px;background:var(--blue);color:#fff}
.foot-brand{position:absolute;left:100px;top:42px;display:flex;align-items:center;gap:10px;font-size:19px}
.foot-brand .brand-dot{width:48px;height:48px;border-color:#fff}
.foot-cta{position:absolute;left:987px;top:58px;width:113px;height:32px;border-radius:16px;background:var(--blue-bright);font-size:13px;font-weight:600;display:flex;align-items:center;justify-content:center}
.rule{position:absolute;left:100px;width:1000px;height:1px;background:rgba(255,255,255,.35)}
.foot-col{position:absolute;top:144px}
.foot-col h5{font-size:13px;font-weight:600;margin-bottom:12px}
.foot-col li{list-style:none;font-size:11px;color:#cfdcf3;margin-bottom:13px}
.socials{position:absolute;left:966px;top:177px;display:grid;grid-template-columns:repeat(3,32px);gap:18px 18px}
.socials span{width:32px;height:32px;border-radius:8px;background:#4f8fe6;display:block}
.copyright{position:absolute;left:0;width:1200px;text-align:center;top:313px;font-size:13px;color:#e6eefb}
</style>
</head>
<body>

<svg width="0" height="0" style="position:absolute"><defs><path id="st" d="M11 1l2.9 6.6 7.1.6-5.4 4.7 1.6 7-6.2-3.7-6.2 3.7 1.6-7L1 8.2l7.1-.6z"/></defs></svg>

<nav class="site-nav">
  <a class="active" style="left:104px">Home</a>
  <a style="left:221px">Services</a>
  <a style="left:351px">About Us</a>
  <div class="brand"><span class="brand-dot"></span>Marrowfen</div>
  <a style="left:888px">Contact</a>
  <div class="support-btn">Support</div>
</nav>

<header class="hero" role="img" aria-label="Glowing fiber optic strands streaking across a dark background">
  <h1 class="hero-title heading">I Beamed Up with <span class="accent">Marrowfen</span><br>Fiber Optics</h1>
  <p class="hero-sub">Experience lightning-fast internet, crystal-clear phone services, and stunning TV options.</p>
  <div class="pill hero-btn">Get Started Today
    <span class="pill-icon" style="background:#fff"><svg width="14" height="16" viewBox="0 0 14 16"><path d="M2 1 L13 8 L2 15Z" fill="#0a4fb0"/></svg></span>
  </div>
</header>

<section class="about">
  <h2 class="heading">About <span class="accent">Us</span></h2>
  <p class="lead">Lorem ipsum dolor sit amet, consectetur adipiscing elit, sed do eiusmod tempor incididunt ut labore et dolore magna aliqua. Ut enim ad minim veniam, quis nostrud exercitation ullamco laboris</p>
  <div class="fact" style="left:103px">
    <h3>The Company's History</h3>
    <p>With over 30 years of experience, starting from dial-up in a basement to building our own fiber optic network</p>
  </div>
  <div class="fact" style="left:389px">
    <h3>The Customer Base</h3>
    <p>Serving residential, business, educational, healthcare, and governmental customers.</p>
  </div>
  <div class="about-photo" role="img" aria-label="Close-up of a network cable plug surrounded by glowing pink and blue fiber optic strands"></div>
  <div class="years">30y</div>
</section>

<section class="services">
  <h2 class="heading"><span class="accent">Services</span> Offered</h2>

  <article class="card card-ghost" style="left:100px;top:283px">
    <svg class="card-icon" style="top:18px" width="68" height="68" viewBox="0 0 68 68" fill="none" stroke="#fff" stroke-width="6"><circle cx="34" cy="34" r="30"/><ellipse cx="34" cy="34" rx="13" ry="30"/><path d="M4 34H64M8 20H60M8 48H60"/></svg>
    <h3 style="top:115px">Internet Services</h3>
    <p style="top:160px">Lorem ipsum dolor sit amet, consectetur adipiscing elit, sed do eiusmod tempor incididunt ut labore et dolore</p>
    <div class="pill btn-white" style="top:249px">Learn More
      <span class="pill-icon" style="background:var(--blue)"><svg width="20" height="16" viewBox="0 0 20 16" fill="none" stroke="#fff" stroke-width="2.2" stroke-linecap="round"><path d="M2 8H18M11 1L18 8L11 15"/></svg></span>
    </div>
  </article>

  <article class="card card-solid" style="left:455px;top:256px">
    <div class="card-icon pill-icon" style="top:12px;width:80px;height:80px;background:var(--blue)">
      <svg width="32" height="32" viewBox="0 0 24 24"><path d="M6.6 10.8a15 15 0 0 0 6.6 6.6l2.2-2.2a1 1 0 0 1 1-.25 11.4 11.4 0 0 0 3.6.57 1 1 0 0 1 1 1V20a1 1 0 0 1-1 1A17 17 0 0 1 3 4a1 1 0 0 1 1-1h3.5a1 1 0 0 1 1 1c0 1.25.2 2.45.57 3.57a1 1 0 0 1-.25 1z" fill="#fff"/></svg>
    </div>
    <h3 style="top:115px">Phone Services</h3>
    <p style="top:160px">Lorem ipsum dolor sit amet, consectetur adipiscing elit, sed do eiusmod tempor incididunt ut labore et dolore</p>
    <div class="pill btn-blue" style="top:249px">Learn More
      <span class="pill-icon" style="background:#fff"><svg width="20" height="16" viewBox="0 0 20 16" fill="none" stroke="#0a4fb0" stroke-width="2.2" stroke-linecap="round"><path d="M2 8H18M11 1L18 8L11 15"/></svg></span>
    </div>
  </article>

  <article class="card card-ghost" style="left:811px;top:283px">
    <svg class="card-icon" style="top:20px" width="78" height="64" viewBox="0 0 78 64" fill="none" stroke="#fff" stroke-width="7"><rect x="4" y="4" width="70" height="46" rx="3"/><path d="M39 50V60M24 60H54"/></svg>
    <h3 style="top:115px">TV Services</h3>
    <p style="top:160px">Lorem ipsum dolor sit amet, consectetur adipiscing elit, sed do eiusmod tempor incididunt ut labore et dolore</p>
    <div class="pill btn-white" style="top:249px">Learn More
      <span class="pill-icon" style="background:var(--blue)"><svg width="20" height="16" viewBox="0 0 20 16" fill="none" stroke="#fff" stroke-width="2.2" stroke-linecap="round"><path d="M2 8H18M11 1L18 8L11 15"/></svg></span>
    </div>
  </article>
</section>

<section class="customers">
  <h2 class="heading">Our Happy <span class="accent">Customers</span></h2>

  <article class="review review-light" style="left:100px">
    <div class="avatar-ring"><div class="avatar" role="img" aria-label="Portrait of a smiling customer" style="background:linear-gradient(160deg,#9fc7b0,#6b7f8e 60%,#3c4a5a)"></div></div>
    <span class="quote" style="left:230px;top:10px">&ldquo;</span>
    <div class="stars" aria-label="Five stars">
      <svg width="142" height="22" viewBox="0 0 142 22"><g fill="#0a4fb0"><use href="#st"/><use href="#st" x="30"/><use href="#st" x="60"/><use href="#st" x="90"/><use href="#st" x="120"/></g></svg>
    </div>
    <h4>Tomas Reval</h4>
    <div class="role" style="font-size:14px;top:182px">Company Founder</div>
    <p style="top:217px">Lorem ipsum dolor sit amet, consectetur adipiscing elit, sed do eiusmod tempor incididunt ut labore et dolore</p>
  </article>

  <article class="review review-dark" style="left:457px">
    <div class="avatar-ring"><div class="avatar" role="img" aria-label="Portrait of a customer" style="background:linear-gradient(160deg,#c9a58a,#9a6a4e 60%,#5a3a2c)"></div></div>
    <div class="stars" aria-label="Five stars">
      <svg width="142" height="22" viewBox="0 0 142 22"><g fill="#fff"><use href="#st"/><use href="#st" x="30"/><use href="#st" x="60"/><use href="#st" x="90"/><use href="#st" x="120"/></g></svg>
    </div>
    <h4>Ilse Varnick</h4>
    <div class="role">Company Founder</div>
    <span class="quote" style="left:118px;top:212px;color:#fff">&ldquo;</span>
    <p style="top:257px">Lorem ipsum dolor sit amet, consectetur adipiscing elit, sed do eiusmod tempor incididunt ut labore et dolore</p>
  </article>

  <article class="review review-light" style="left:813px">
    <div class="avatar-ring"><div class="avatar" role="img" aria-label="Photo of a couple outdoors under a pink sky" style="background:linear-gradient(180deg,#e99bb6,#c9a9c4 45%,#7a8a6a 75%,#4a5a3e)"></div></div>
    <div class="stars" aria-label="Five stars">
      <svg width="142" height="22" viewBox="0 0 142 22"><g fill="#0a4fb0"><use href="#st"/><use href="#st" x="30"/><use href="#st" x="60"/><use href="#st" x="90"/><use href="#st" x="120"/></g></svg>
    </div>
    <h4>Mara Quillen</h4>
    <div class="role">Company Founder</div>
    <span class="quote" style="left:118px;top:212px">&ldquo;</span>
    <p style="top:257px">Lorem ipsum dolor sit amet, consectetur adipiscing elit, sed do eiusmod tempor incididunt ut labore et dolore</p>
  </article>

  <div class="cta" role="img" aria-label="Blue panel with streaking light lines">
    <h2 class="heading">We Are happy To Hear You</h2>
    <p>Lorem ipsum dolor sit amet, consectetur adipiscing elit, sed do eiusmod tempor incididunt ut labore et dolore magna aliqua. Ut enim ad minim veniam, quis nostrud exercitation ullamco laboris</p>
    <div class="pill">Send Us A Message
      <span class="pill-icon" style="background:var(--blue-bright)"><svg width="18" height="14" viewBox="0 0 18 14"><rect x="0" y="0" width="18" height="14" rx="2" fill="#fff"/><path d="M1 2L9 8L17 2" fill="none" stroke="#0d63c4" stroke-width="1.8"/></svg></span>
    </div>
  </div>
</section>

<footer class="site-footer">
  <div class="foot-brand"><span class="brand-dot"></span>Marrowfen's</div>
  <div class="foot-cta">Get Started</div>
  <div class="rule" style="top:114px"></div>
  <div class="foot-col" style="left:100px"><h5>Marrowfen's</h5><ul><li>About us</li><li>Customers</li></ul></div>
  <div class="foot-col" style="left:340px"><h5>Our Services</h5><ul><li>Internet Services</li><li>Phone Services</li><li>TV Services</li></ul></div>
  <div class="foot-col" style="left:601px"><h5>Support</h5><ul><li>+1 555-014-2270</li><li>help@brimvane.com</li></ul></div>
  <div class="foot-col" style="left:990px"><h5>Social Media</h5></div>
  <div class="socials" aria-label="Social media links"><span></span><span></span><span></span><span></span><span></span><span></span></div>
  <div class="rule" style="top:286px"></div>
  <div class="copyright">@2024 Copyright • all rights reserved</div>
</footer>

</body>
</html>
```